Website Design for Agency

We require a website for our new agency. We have created a brief with our content, copywriting and most graphical assets. We just need some great with layout and to add some flair.
Updates

Went on vacation/holiday

Number of Pages Required

1 page

Font styles to use
Sans Serif

```html
<!DOCTYPE html>
<html lang="en">
<head>
<meta charset="utf-8">
<title>Case Study Agency</title>
<link href="https://fonts.googleapis.com/css2?family=Poppins:wght@400;500;600&display=swap" rel="stylesheet">
<style>
:root{
  --ink:#111111;
  --text:#2a2a2a;
  --muted:#555555;
  --yellow:#f7e06a;
  --soft:#f3f3f3;
  --line:#dddddd;
  --white:#ffffff;
  --nav:#2d3a6b;
  --mauve:#b9a9a7;
}
*{margin:0;padding:0;box-sizing:border-box}
html,body{width:1200px;height:5222px;overflow:hidden}
body{position:relative;font-family:'Poppins',sans-serif;color:var(--text);background:var(--white)}
.abs{position:absolute}
.hero-bg{left:0;top:0;width:1200px;height:560px;background:linear-gradient(#f0f0f0,#ffffff)}
.logo{left:126px;top:38px;display:flex;align-items:center;gap:8px;font-size:19px;font-weight:600;color:var(--nav)}
.logo i{width:24px;height:24px;border-radius:50%;background:var(--ink);display:block}
.nav{left:438px;top:42px;display:flex;gap:34px;font-size:13px;color:var(--nav)}
.btn{display:inline-flex;align-items:center;justify-content:center;background:var(--ink);color:var(--white);border-radius:22px;font-size:12px;font-weight:500;height:42px;padding:0 30px;white-space:nowrap}
.btn-call{left:939px;top:30px;width:132px;padding:0}
h1{font-size:40px;line-height:44px;font-weight:500;color:var(--ink)}
h2{font-size:32px;line-height:44px;font-weight:500;color:var(--ink)}
p.copy{font-size:12.5px;line-height:22px;color:var(--text)}
.link{display:inline-flex;align-items:center;gap:8px;font-size:12.5px;font-weight:500;color:var(--ink);white-space:nowrap}
.art{border-radius:12px}
.band{left:389px;top:612px;width:811px;height:143px;background:var(--ink);display:flex;align-items:center;justify-content:space-between;padding:0 30px;color:var(--white)}
.partners{display:flex;gap:34px;align-items:center}
.partner{display:flex;align-items:center;gap:7px;font-size:11px;font-weight:600;letter-spacing:1.5px;white-space:nowrap}
.partner span{width:13px;height:13px;border:2px solid var(--white);border-radius:50%;flex:none}
.video{left:669px;top:1662px;width:386px;height:213px;background:#2b2b2b;box-shadow:0 8px 18px rgba(0,0,0,.18)}
.video-bar{position:absolute;left:0;bottom:0;width:100%;height:26px;background:var(--white);display:flex;align-items:center;padding:0 14px;gap:10px}
.video-bar .track{flex:1;height:2px;background:#ddd;position:relative}
.video-bar .track b{position:absolute;left:0;top:0;width:30%;height:2px;background:#e36a6a}
.play{position:absolute;left:172px;top:71px;width:42px;height:42px;border-radius:50%;background:var(--white);display:flex;align-items:center;justify-content:center}
.rule{left:126px;width:946px;height:1px;background:var(--line)}
.center{left:0;width:1200px;text-align:center}
.card{width:215px;height:156px;border-radius:4px;background:var(--ink);color:var(--white);padding:22px 22px;font-size:12px;line-height:16px;display:flex;flex-direction:column;gap:22px}
.card.yellow{background:var(--yellow);color:var(--ink)}
.card .tick{width:18px;height:18px;border:1.5px solid currentColor;border-radius:50%;display:flex;align-items:center;justify-content:center}
.pricing-bg{left:0;top:4324px;width:1200px;height:784px;background:var(--soft)}
.plan{width:223px;height:361px;background:var(--white);border-radius:8px;overflow:hidden;box-shadow:0 4px 12px rgba(0,0,0,.08)}
.plan-head{height:183px;background:var(--ink);color:var(--white);text-align:center;padding-top:34px}
.plan-head .name{font-size:15px}
.plan-head .price{font-size:30px;font-weight:500;line-height:40px}
.plan-head .per{font-size:15px}
.plan ul{list-style:none;padding:24px 0 0 60px;font-size:12px;line-height:31px;color:var(--ink)}
.plan li::before{content:"✓";margin-right:10px;font-size:11px}
.footer{left:0;top:5108px;width:1200px;height:114px;background:var(--ink);color:var(--white)}
.footer-nav{position:absolute;left:158px;top:38px;display:flex;gap:32px;font-size:13px}
.follow{position:absolute;left:845px;top:32px;font-size:12px}
.socials{display:flex;gap:14px;margin-top:8px}
.socials span{width:18px;height:18px;border-radius:50%;background:#2a6fd1;display:block}
</style>
</head>
<body>

<div class="abs hero-bg"></div>

<header>
  <div class="abs logo"><i></i>Your Logo</div>
  <nav class="abs nav"><span>Home</span><span>Services</span><span>How it works</span><span>Examples</span><span>Contact</span></nav>
  <div class="abs btn btn-call">Schedulle a call</div>
</header>

<section>
  <h1 class="abs" style="left:126px;top:158px;width:480px">Win More Hearts with Powerful Case Studies</h1>
  <p class="abs copy" style="left:126px;top:268px;width:430px">Testimonial Videos, written PDF's, slides, one-pagers and social media content. We create spellbinding case study stories and videos that will drive business for your revenue team . No more writing, proofing organizing videographers and time-consuming hassles. We'll handle everything 100% and deliver to you powerful marketing assets you'll be proud to share.</p>
  <div class="abs btn" style="left:126px;top:441px;width:134px;padding:0">Learn more</div>
  <div class="abs link" style="left:296px;top:454px">Watch Video
    <svg width="18" height="18" viewBox="0 0 18 18"><circle cx="9" cy="9" r="8" fill="none" stroke="#111" stroke-width="1.4"/><path d="M7 5.5l5 3.5-5 3.5z" fill="#111"/></svg></div>
  <div class="abs art" role="img" aria-label="Line illustration of a person riding a rising arrow chart" style="left:650px;top:140px;width:405px;height:357px;background:linear-gradient(135deg,#f5f5f5,#e9e9e9)"></div>
</section>

<section>
  <div class="abs" style="left:126px;top:654px;font-size:17px;line-height:28px;font-weight:500;color:var(--ink)">Trusted by hundred<br>companies</div>
  <div class="abs band">
    <svg width="22" height="16" viewBox="0 0 22 16"><path d="M21 8H2M8 2L2 8l6 6" fill="none" stroke="#fff" stroke-width="1.6"/></svg>
    <div class="partners">
      <div class="partner"><span></span>LINKWELL</div>
      <div class="partner"><span></span>LOOPLINE</div>
      <div class="partner"><span></span>BRIGHTFRAME</div>
      <div class="partner"><span></span>SHUTTER GUILD</div>
      <div class="partner"><span></span>BRIGHTFRAME</div>
    </div>
    <svg width="22" height="16" viewBox="0 0 22 16"><path d="M1 8h19M14 2l6 6-6 6" fill="none" stroke="#fff" stroke-width="1.6"/></svg>
  </div>
</section>

<section>
  <h2 class="abs" style="left:126px;top:850px;width:470px">Capture results, built trust and win new business</h2>
  <p class="abs copy" style="left:134px;top:968px;width:420px">Combining real-world results with social proof, one well-produced customer story with multiple marketing assets will do a LOT of the heavy lifting for your business sales...because it comes directly from the mouth of a happy human who loves what you do</p>
  <div class="abs art" role="img" aria-label="Illustration of a person working at a laptop in front of a yellow circle" style="left:700px;top:812px;width:360px;height:296px;background:radial-gradient(circle at 45% 45%,var(--yellow) 0 34%,#f6f6f6 35%)"></div>
</section>

<section>
  <div class="abs art" role="img" aria-label="Illustration of two people arranging charts on a wall, yellow circle behind" style="left:162px;top:1186px;width:324px;height:304px;background:radial-gradient(circle at 52% 55%,var(--yellow) 0 36%,#f6f6f6 37%)"></div>
  <h2 class="abs" style="left:624px;top:1234px">It’s More Than Marketing</h2>
  <p class="abs copy" style="left:630px;top:1300px;width:425px">No more awful sales sheets and dull corporate announcements that tell people to spend their money without reason. Our team of Laurel®-winning journalists ensure your case studies are authentic. They're real. They're raw. They give people a reason to trust you, and, more importantly, a reason to give you their business.</p>
</section>

<section>
  <h2 class="abs" style="left:134px;top:1636px;width:420px">Get a testimonial video anywhere nationwide</h2>
  <p class="abs copy" style="left:134px;top:1754px;width:410px">You get our team of pros to handle the outreach, the interviews, the field production (or remote) and all the editing, graphics and storytelling for a lot less than you think. Powerful, proven content that moves the needle.</p>
  <div class="abs link" style="left:134px;top:1890px">Plans and Pricing <span>→</span></div>
  <div class="abs btn" style="left:300px;top:1877px;width:134px;padding:0">Learn more</div>
  <div class="abs video">
    <div class="play"><svg width="16" height="18" viewBox="0 0 16 18"><path d="M2 1l13 8-13 8z" fill="#2b2b2b"/></svg></div>
    <div class="video-bar">
      <svg width="8" height="8" viewBox="0 0 8 8"><path d="M1 0l6 4-6 4z" fill="#333"/></svg>
      <svg width="10" height="8" viewBox="0 0 10 8"><path d="M1 0v8M3 0l6 4-6 4z" fill="#333" stroke="#333"/></svg>
      <div class="track"><b></b></div>
      <svg width="10" height="8" viewBox="0 0 10 8"><path d="M0 2h3l3-2v8L3 6H0z" fill="#333"/></svg>
      <svg width="9" height="9" viewBox="0 0 9 9"><circle cx="4.5" cy="4.5" r="3.5" fill="none" stroke="#333" stroke-width="2"/></svg>
    </div>
  </div>
</section>

<section>
  <div class="abs art" role="img" aria-label="Collage of case study documents, social posts and a video thumbnail" style="left:146px;top:2013px;width:320px;height:324px;background:linear-gradient(135deg,#e8eef8,#f6f6f6 60%,#e4ecf7)"></div>
  <h2 class="abs" style="left:612px;top:2034px;width:460px">Don’t settle for just a single case study. Get a lot more.</h2>
  <p class="abs copy" style="left:612px;top:2144px;width:430px">Narrative stories with your customer as the hero is key to readability and persuasion. Get professionally wordsmithed case studies to upload to your website, social channels, and more with pride.</p>
  <div class="abs link" style="left:612px;top:2247px">Plans and Pricing <span>→</span></div>
  <div class="abs btn" style="left:790px;top:2234px;width:134px;padding:0">Learn more</div>
</section>

<section>
  <h2 class="abs" style="left:126px;top:2440px">Promo &amp; Sales Collateral</h2>
  <p class="abs copy" style="left:126px;top:2500px;width:410px">From one-sheets, slides, long, short, and ultra-short articles for your website, blog, or sales team. You are in good hands knowing the content you get back is marketing gold. All without the headaches</p>
  <div class="abs link" style="left:126px;top:2614px">Plans and Pricing <span>→</span></div>
  <div class="abs" role="img" aria-label="Photo of open brochures with interior design spreads on a mauve surface" style="left:584px;top:2428px;width:481px;height:298px;background:linear-gradient(135deg,#c4b4b2,var(--mauve))"></div>
</section>

<section>
  <div class="abs art" role="img" aria-label="Illustration of a team meeting around a table with a presentation board" style="left:146px;top:2797px;width:405px;height:294px;background:radial-gradient(circle at 45% 45%,var(--yellow) 0 30%,#f6f6f6 31%)"></div>
  <h2 class="abs" style="left:612px;top:2812px;width:450px">Need help promoting your customer story? We got you.</h2>
  <p class="abs copy" style="left:612px;top:2972px;width:425px">You get campaign level help from our team. Landing pages, lead capture forms, press releases &amp; PR outreach to 400+ organizations and 100,000 journalists. All done by former our in-house former reporters who know how it's done.</p>
  <div class="abs link" style="left:612px;top:3091px">Plans and Pricing <span>→</span></div>
  <div class="abs btn" style="left:790px;top:3078px;width:134px;padding:0">Learn more</div>
</section>

<div class="abs rule" style="top:3215px"></div>

<section>
  <h2 class="abs center" style="top:3280px;font-size:38px;line-height:54px">100% stress-free case study<br>project management</h2>
  <h3 class="abs" style="left:130px;top:3536px;font-size:24px;font-weight:500;color:var(--ink)">Get More for Less</h3>
  <p class="abs copy" style="left:130px;top:3592px;width:390px">Whether you manage the marketing yourself or or have an in-house marketing manager, getting case studies done can be time consuming and costly if you don't do it right. We believe partnering with a case study expert can help your business prosper and establish itself as an industry leader.</p>
  <div class="abs art" role="img" aria-label="Line illustration of a person relaxing with a laptop under a palm tree at sunset" style="left:669px;top:3436px;width:386px;height:304px;background:linear-gradient(180deg,#f6f6f6,#f0f0f0)"></div>
</section>

<div class="abs rule" style="top:3790px"></div>

<section>
  <h2 class="abs center" style="top:3846px;font-size:29px">Free up your schedule</h2>
  <p class="abs center copy" style="top:3904px">Our team of experienced video producers and content creators use proven<br>persuasion strategies to create attention-grabbing case studies.</p>
  <div class="abs card yellow" style="left:126px;top:3983px"><span class="tick"><svg width="9" height="7" viewBox="0 0 9 7"><path d="M1 3.5l2.5 2.5L8 1" fill="none" stroke="currentColor" stroke-width="1.4"/></svg></span>We provide respectful and proactive client management throughout each case study project.</div>
  <div class="abs card" style="left:371px;top:3983px"><span class="tick"><svg width="9" height="7" viewBox="0 0 9 7"><path d="M1 3.5l2.5 2.5L8 1" fill="none" stroke="currentColor" stroke-width="1.4"/></svg></span>We produce quality assets that your client will love and protect your brand's reputation.</div>
  <div class="abs card" style="left:614px;top:3983px"><span class="tick"><svg width="9" height="7" viewBox="0 0 9 7"><path d="M1 3.5l2.5 2.5L8 1" fill="none" stroke="currentColor" stroke-width="1.4"/></svg></span>We save you countless hours of time and effort.</div>
  <div class="abs card" style="left:857px;top:3983px"><span class="tick"><svg width="9" height="7" viewBox="0 0 9 7"><path d="M1 3.5l2.5 2.5L8 1" fill="none" stroke="currentColor" stroke-width="1.4"/></svg></span>We ensure your satisfaction with every piece of case study material we deliver.</div>
  <div class="abs btn" style="left:533px;top:4203px;width:132px;height:38px;padding:0">Get in touch</div>
</section>

<section>
  <div class="abs pricing-bg"></div>
  <p class="abs center" style="top:4372px;font-size:17px;color:var(--ink)">Plans &amp; Pricing</p>
  <h2 class="abs center" style="top:4414px;font-size:34px">Everything you need is right here</h2>
  <p class="abs center" style="top:4480px;font-size:17px;line-height:28px;color:var(--ink)">Avoid the headaches over case study copywriting<br>and testimonial video production.</p>
  <div class="abs btn" style="left:548px;top:4572px;width:132px;height:38px;padding:0">Get in touch</div>

  <div class="abs plan" style="left:130px;top:4666px"><div class="plan-head"><div class="name">Starter</div><div class="price">$200</div><div class="per">/Month</div></div><ul><li>Benefit one</li><li>Benefit two</li><li>Benefit three</li><li>Benefit four</li><li>Benefit five</li></ul></div>
  <div class="abs plan" style="left:371px;top:4666px"><div class="plan-head"><div class="name">Business</div><div class="price">$200</div><div class="per">/Month</div></div><ul><li>Benefit one</li><li>Benefit two</li><li>Benefit three</li><li>Benefit four</li><li>Benefit five</li></ul></div>
  <div class="abs plan" style="left:612px;top:4666px"><div class="plan-head"><div class="name">Pro</div><div class="price">$200</div><div class="per">/Month</div></div><ul><li>Benefit one</li><li>Benefit two</li><li>Benefit three</li><li>Benefit four</li><li>Benefit five</li></ul></div>
  <div class="abs plan" style="left:851px;top:4666px"><div class="plan-head"><div class="name">Enterprise</div><div class="price">$200</div><div class="per">/Month</div></div><ul><li>Benefit one</li><li>Benefit two</li><li>Benefit three</li><li>Benefit four</li><li>Benefit five</li></ul></div>
</section>

<footer class="abs footer">
  <nav class="footer-nav"><span>Home</span><span>Services</span><span>How it works</span><span>Examples</span><span>Contact</span></nav>
  <div class="follow">Follow Us
    <div class="socials" aria-label="Social links"><span></span><span></span><span></span><span></span></div>
  </div>
</footer>

</body>
</html>
```